business card for Franco-Turkish restaurant

We are a Franco-Turkish restaurant, Le Coquelicot, based in the Cotes d'Armor in Brittany, near the Pink Granite Coast. We serve mainly Turkish cuisine. We would like a card reminding Britain and Turkey. No flag. Color: turquoise (sea ..), green, red. There should be a space for 3 lines: name, address, phone / email

Industry/Entity Type

Fast Food Restaurant

Contact Information for Business Card

Dervan Oruzel
Addresse: 14 Rue Paul-Henri Dauvel, 22410 Kervalou, France
Tel:+33 2 96 47 83 09

Colors
33a6d7
f04a50
acd036

Nice to have
• Symbols of Britain and Turkey
Should not have
• No flags

```html
<!DOCTYPE html>
<html lang="fr">
<head>
<meta charset="utf-8">
<title>Le Coquelicot – carte de visite</title>
<link rel="stylesheet" href="https://fonts.googleapis.com/css2?family=Raleway:wght@300;400&display=swap">
<style>
  :root {
    --backdrop: #2b2119;
    --teal-light: #5b9c9e;
    --teal: #3f8486;
    --teal-dark: #2d6668;
    --poppy: #c8161e;
    --poppy-light: #d8232b;
    --meadow: #acd036;
    --ink-light: #f3eeee;
  }
  * { margin: 0; padding: 0; box-sizing: border-box; }
  html, body {
    width: 1200px;
    height: 900px;
    overflow: hidden;
    background: var(--backdrop);
  }
  .canvas {
    position: relative;
    width: 1200px;
    height: 900px;
  }
  .business-card {
    position: absolute;
    left: 120px;
    top: 170px;
    width: 960px;
    height: 560px;
    overflow: hidden;
    background: radial-gradient(ellipse at 55% 35%, var(--teal-light) 0%, var(--teal) 45%, var(--teal-dark) 100%);
    box-shadow: 0 18px 40px rgba(0, 0, 0, 0.45);
    font-family: "Raleway", sans-serif;
  }
  .brand {
    position: absolute;
    left: 0;
    right: 0;
    top: 140px;
    display: flex;
    flex-direction: column;
    align-items: center;
    padding-left: 140px;
  }
  .brand-row {
    display: flex;
    align-items: center;
    gap: 18px;
  }
  .brand-dot {
    width: 26px;
    height: 26px;
    border-radius: 50%;
    background: var(--poppy);
  }
  .brand-name {
    font-weight: 300;
    font-size: 64px;
    letter-spacing: 1px;
    color: var(--ink-light);
  }
  .brand-tagline {
    margin-top: 6px;
    font-weight: 300;
    font-size: 22px;
    letter-spacing: 9px;
    color: var(--ink-light);
  }
  .brand-rule {
    display: block;
    margin-top: 18px;
    width: 300px;
    height: 4px;
    border-radius: 2px;
    background: var(--meadow);
  }
  .contact-band {
    position: absolute;
    left: 0;
    right: 0;
    bottom: 0;
    height: 168px;
    background: linear-gradient(180deg, var(--poppy-light), var(--poppy));
    border-top: 6px solid var(--meadow);
  }
  .contact-list {
    position: absolute;
    left: 360px;
    top: 18px;
    list-style: none;
    font-weight: 300;
    font-size: 19px;
    line-height: 30px;
    color: var(--ink-light);
  }
</style>
</head>
<body>
<main class="canvas">
  <section class="business-card">
    <div class="brand">
      <div class="brand-row">
        <span class="brand-dot"></span>
        <span class="brand-name">Le Coquelicot</span>
      </div>
      <span class="brand-tagline">Restaurant</span>
      <span class="brand-rule"></span>
    </div>
    <div class="contact-band">
      <ul class="contact-list">
        <li>Dervan Oruzel</li>
        <li>14 Rue Paul-Henri Dauvel, 22410 Kervalou</li>
        <li>Tel: +33 2 96 47 83 09</li>
        <li>Email: dervan@coquelicot-kervalou.fr</li>
      </ul>
    </div>
  </section>
</main>
</body>
</html>
```